R&D and Engineering Management Consultancy Needs Branding

I need a branding style for my consultancy - specifically I need business cards by Tuesday 26 April (9 days away!) to take to a conference, including a logo design. If this service does not include printing I will need it in time for printing.

Later, the same logo and style needs to be incorporated into a Powerpoint template and a Word Template. Optionally also a Pages template.

The branding image needs to project and/or support the following qualities:
High tech
Speed and throughput
Lean
Innovation
Dependability
Quality

One possible concept is based on the Principal’s surname – Marrowby, which is a small bird. So a logo design which is a stylized rendition of a bird may work well. Flight implies speed, and the style would be “techy”, perhaps geometric in a way that conveys Lean – boiling things down to the essential elements.

Other concepts are welcome.
You can find me on https://au.peoplenexa.com/in/hollismarrowby

Business Card Information
Marrowby Consulting
Hollis Marrowby
BE (Hons), CSM, CSPO, SA
Principal Consultant
Mobile: +61 (0)455 913 607
Email: hollis@marrowbyconsulting.com
Web: www.marrowbyconsulting.com

Reverse:
Lean/Agile Software Development at Scale
Lean Product Development
Lean Portfolio Management
Organisational development and transformation
Mentoring and coaching of Technical Leaders
Program and project management
Business Processes and Systems

Target Market(s)

The target market for this consultancy comprises technology-based product and/or services development companies. They typically engage in one or a mix of software, electronics, mechanical, ASIC and MEMS development activities. They range from small startups to transnational corporations staffed by highly skilled engineers, developers and scientists. The consultancy is applicable across a range of domains such as biomedical device development, inkjet printing technology, telecommunications, internet and mesh networking technologies, renewable energy systems, and electronic product development of all kinds.

Industry/Entity Type

Information Technology

Contact Information for Business Card

Marrowby Consulting
Hollis Marrowby
BE (Hons), CSM, CSPO, SA
Principal Consulting

Reverse:
➢ Lean/Agile Software Development
➢ Lean Product Development
➢ Lean Portfolio Management
➢ Organisational development and transformation
➢ Mentoring and coaching of Technical Leaders
➢ Program and project management
➢ Business Processes and Systems

Logo Text

Just graphical

Font styles to use
Sans Serif

Requirements
Must have
• A clean professional look
Nice to have
• Use a bird motif based on my name Marrowby
• The bird's colours are yellow/gold, light brown, black and red so these suggest a colour scheme.
• I have uploaded a stylised bird design that I like but this belongs to another company. A variation on this might be good.
Should not have
• Too much clutter. If the details are too much to fit, drop the qualifications line

```html
<!DOCTYPE html>
<html lang="en">
<head>
<meta charset="utf-8">
<title>Marrowby Consulting — Business Cards</title>
<link rel="stylesheet" href="https://fonts.googleapis.com/css2?family=Open+Sans:wght@400;600&display=swap">
<style>
  :root {
    --gold-bright: #f8f400;
    --gold-mid: #e2d800;
    --gold-deep: #c6b500;
    --gold-text: #d4c400;
    --ink: #1c1c1c;
    --paper: #ffffff;
    --backdrop: #ecebe6;
  }
  * { box-sizing: border-box; margin: 0; padding: 0; }
  html, body { width: 1200px; height: 900px; overflow: hidden; }
  body {
    position: relative;
    background: var(--backdrop);
    font-family: "Open Sans", Arial, sans-serif;
    color: var(--ink);
  }
  .card {
    position: absolute;
    border-radius: 18px;
    overflow: hidden;
    background: var(--paper);
    box-shadow: 0 6px 18px rgba(0,0,0,0.12);
  }
  .card--front { left: 78px; top: 35px; width: 588px; height: 363px; }
  .card--back  { left: 389px; top: 506px; width: 566px; height: 350px; }

  .band {
    position: absolute; left: 0; right: 0;
    background: linear-gradient(to bottom, var(--gold-bright), var(--gold-deep));
  }
  .card--front .band { top: 40px; height: 100px; }

  .mark-square {
    position: absolute;
    width: 82px; height: 82px;
  }
  .card--front .mark-square { left: 259px; top: 42px; background: var(--paper); }
  .card--back .mark-square  { left: 242px; top: 89px; background: var(--gold-bright); }

  .wordmark {
    position: absolute; left: 0; right: 0;
    text-align: center;
    font-weight: 400;
    text-transform: uppercase;
    line-height: 1;
  }
  .wordmark__name { display: block; font-size: 34px; letter-spacing: 2px; }
  .wordmark__sub  { display: block; font-size: 18px; letter-spacing: 2px; margin-top: 6px; }
  .card--front .wordmark { top: 172px; color: var(--gold-text); }
  .card--back .wordmark  { top: 202px; color: var(--paper); }

  .person { position: absolute; left: 20px; top: 254px; }
  .person__name { font-size: 19px; font-weight: 600; color: var(--gold-text); line-height: 1.2; }
  .person__line { font-size: 15px; line-height: 1.45; margin-top: 4px; }
  .person__line + .person__line { margin-top: 0; }

  .contacts {
    position: absolute; right: 36px; top: 257px;
    list-style: none; text-align: right;
    font-size: 15px; line-height: 25px;
  }
  .contacts li { position: relative; padding-right: 22px; }
  .contacts svg { position: absolute; right: 0; top: 6px; width: 13px; height: 13px; }

  .card--back { background: linear-gradient(to bottom, var(--gold-bright) 0%, var(--gold-mid) 50%, var(--gold-deep) 100%); }
  .card--back .stripe { position: absolute; left: 0; right: 0; top: 81px; height: 96px; background: var(--paper); }
</style>
</head>
<body>

<section class="card card--front" aria-label="Business card front">
  <div class="band"></div>
  <div class="mark-square"></div>
  <div class="wordmark">
    <span class="wordmark__name">Marrowby</span>
    <span class="wordmark__sub">Consulting</span>
  </div>
  <div class="person">
    <p class="person__name">Hollis Marrowby</p>
    <p class="person__line">BE (Hons), CSM, CSPO, SA</p>
    <p class="person__line">Principal Consulting</p>
  </div>
  <ul class="contacts">
    <li>+61 (0)455 913 607
      <svg viewBox="0 0 16 16" aria-hidden="true"><path fill="#e0d000" d="M3 1l3 3-1.5 2c1 2 3 4 5 5L11.5 9.5l3 3L13 15C7 14 2 9 1 3z"/></svg>
    </li>
    <li>hollis@marrowbyconsulting.com
      <svg viewBox="0 0 16 16" aria-hidden="true"><rect x="1" y="3" width="14" height="10" fill="#e0d000"/><path d="M1 3l7 6 7-6" stroke="#fff" stroke-width="1.3" fill="none"/></svg>
    </li>
    <li>www.marrowbyconsulting.com
      <svg viewBox="0 0 16 16" aria-hidden="true"><circle cx="8" cy="8" r="7" fill="#e0d000"/></svg>
    </li>
  </ul>
</section>

<section class="card card--back" aria-label="Business card back">
  <div class="stripe"></div>
  <div class="mark-square"></div>
  <div class="wordmark">
    <span class="wordmark__name">Marrowby</span>
    <span class="wordmark__sub">Consulting</span>
  </div>
</section>

</body>
</html>
```